Australian Software Consultancy needs new Business Card Design

Design Business Card based on existing design artefacts (attached). We are open to all designs. As its a 2 sided design and we thought it might be quite striking to have one side with a black background and te other side with a white background.

Target Market(s)

Financial Services mainly.

Industry/Entity Type

Business

Contact Information for Business Card

Name :
Position :
Email :

Requirements
Must have
• Funky design using our existing assets

```html
<!DOCTYPE html>
<html lang="en">
<head>
<meta charset="utf-8">
<title>Northlake Logic – Business Card</title>
<link rel="stylesheet" href="https://fonts.googleapis.com/css2?family=Montserrat:wght@500;600;700&display=swap">
<style>
  :root {
    --backdrop: #d9d9d9;
    --backdrop-light: #e9e9e9;
    --card: #ffffff;
    --ink: #141414;
    --accent: #e8202a;
    --shadow: rgba(0, 0, 0, 0.32);
  }
  * { margin: 0; padding: 0; box-sizing: border-box; }
  html, body {
    width: 1200px;
    height: 1000px;
    overflow: hidden;
    background: linear-gradient(180deg, var(--backdrop) 0%, var(--backdrop-light) 100%);
    font-family: "Montserrat", Arial, sans-serif;
  }
  .canvas {
    position: relative;
    width: 1200px;
    height: 1000px;
  }
  .card {
    position: absolute;
    top: 75px;
    width: 431px;
    height: 240px;
    background: var(--card);
    overflow: hidden;
    box-shadow: 8px 12px 24px var(--shadow);
  }
  .card--front { left: 111px; }
  .card--back { left: 641px; }

  .brand__name {
    position: absolute;
    left: 42px;
    top: 175px;
    font-size: 24px;
    line-height: 30px;
    font-weight: 700;
    letter-spacing: 0.3px;
    color: var(--ink);
    white-space: nowrap;
  }
  .brand__disc {
    position: absolute;
    left: 300px;
    top: -20px;
    width: 250px;
    height: 250px;
    border-radius: 50%;
    background: var(--accent);
  }

  .contact {
    position: absolute;
    right: 32px;
    top: 140px;
    text-align: right;
  }
  .contact__name {
    font-size: 16px;
    line-height: 20px;
    font-weight: 700;
    letter-spacing: 1px;
    color: var(--ink);
  }
  .contact__role {
    margin-top: 2px;
    font-size: 9.5px;
    line-height: 12px;
    font-weight: 500;
    letter-spacing: 1.4px;
    color: var(--accent);
  }
  .contact__email {
    margin-top: 13px;
    font-size: 12px;
    line-height: 16px;
    font-weight: 600;
    color: var(--ink);
  }
</style>
</head>
<body>
  <main class="canvas">
    <section class="card card--front" aria-label="Card front">
      <span class="brand__disc"></span>
      <p class="brand__name">NORTHLAKE LOGIC</p>
    </section>

    <section class="card card--back" aria-label="Card back">
      <div class="contact">
        <p class="contact__name">JOHN DOE</p>
        <p class="contact__role">MANAGING DIRECTOR</p>
        <p class="contact__email">johndoe@northlakelogic.com</p>
      </div>
    </section>
  </main>
</body>
</html>
```